Business Card Design - Law Firm

I need a business card design. I have attached a picture of the law firm's website and logo. The business card design should be consistent with those pictures. There should be a place for the employee name, employee job title, telephone number, facsimile number, address, website url, and email address for each employee.
Industry/Entity Type
Business

```html
<!DOCTYPE html>
<html lang="en">
<head>
<meta charset="UTF-8">
<title>Wexford Law – Business Card</title>
<link href="https://fonts.googleapis.com/css2?family=Libre+Bodoni:ital,wght@0,400;1,700&display=swap" rel="stylesheet">
<style>
  :root {
    --page: #ffffff;
    --card-cream: #e6e5c0;
    --card-band: #c9c8a2;
    --sage: #7a7d5c;
    --sage-deep: #5d6045;
    --gold: #a8942a;
    --ink: #1e1f1c;
    --mark: #1e2124;
    --white: #ffffff;
  }
  html, body {
    margin: 0;
    padding: 0;
    width: 1200px;
    height: 788px;
    overflow: hidden;
    background: var(--page);
  }
  .business-card {
    position: absolute;
    left: 75px;
    top: 106px;
    width: 1057px;
    height: 622px;
    background: var(--card-cream);
    overflow: hidden;
    box-shadow: -3px 2px 3px rgba(0,0,0,0.12);
  }
  .card-shapes {
    position: absolute;
    inset: 0;
  }
  .brand {
    position: absolute;
    left: 68px;
    top: 58px;
    display: flex;
    align-items: center;
    gap: 26px;
  }
  .brand-square {
    width: 104px;
    height: 104px;
    background: var(--mark);
  }
  .brand-name {
    font-family: "Libre Bodoni", "Bodoni Moda", serif;
    font-weight: 400;
    font-size: 54px;
    color: var(--gold);
    line-height: 1;
    white-space: nowrap;
  }
  .employee {
    position: absolute;
    left: 658px;
    top: 76px;
    width: 340px;
    font-family: "Libre Bodoni", serif;
    font-style: italic;
    font-weight: 700;
    color: var(--white);
  }
  .employee-name {
    margin: 0;
    font-size: 29px;
    line-height: 1.1;
  }
  .employee-title {
    margin: 10px 0 0;
    font-size: 26px;
    line-height: 1.1;
    text-align: right;
    width: 262px;
  }
  .contact-list {
    position: absolute;
    left: 74px;
    top: 408px;
    margin: 0;
    padding: 0;
    list-style: none;
    font-family: "Libre Bodoni", serif;
    font-style: italic;
    font-weight: 700;
    font-size: 27px;
    letter-spacing: 1.2px;
    line-height: 38px;
    color: var(--ink);
  }
</style>
</head>
<body>
  <section class="business-card">
    <svg class="card-shapes" width="1057" height="622" viewBox="0 0 1057 622" aria-hidden="true">
      <defs>
        <linearGradient id="band-shade" x1="0" y1="0" x2="0" y2="1">
          <stop offset="0" stop-color="var(--card-cream)" stop-opacity="0"/>
          <stop offset="0.8" stop-color="#bfbe98" stop-opacity="0.9"/>
          <stop offset="1" stop-color="#d4d3ad" stop-opacity="0.6"/>
        </linearGradient>
        <filter id="arc-shadow" x="-20%" y="-20%" width="140%" height="140%">
          <feGaussianBlur stdDeviation="14"/>
        </filter>
      </defs>
      <rect x="0" y="255" width="1057" height="42" fill="url(#band-shade)"/>
      <path d="M611,0 C548,70 545,205 630,310 C735,440 895,520 1057,523 L1057,0 Z"
            fill="var(--sage-deep)" opacity="0.55" filter="url(#arc-shadow)"/>
      <path d="M626,0 C568,65 562,200 644,300 C742,425 900,508 1057,513 L1057,0 Z"
            fill="var(--sage)"/>
    </svg>

    <div class="brand">
      <div class="brand-square"></div>
      <span class="brand-name">Wexford Law</span>
    </div>

    <div class="employee">
      <p class="employee-name">Employee Name</p>
      <p class="employee-title">Job Title</p>
    </div>

    <ul class="contact-list">
      <li>Phone:</li>
      <li>Facsimile::</li>
      <li>Address:</li>
      <li>e-mail:</li>
      <li>website:</li>
    </ul>
  </section>
</body>
</html>
```